GPS SALES

Lopoking to design a website for my company " Marbury Designs"
Our slogan is "GPS that's shaped to suit"

I sell in dash gps systems for cars that are built into the dash board. No gaps after install. designed specifically for specific cars.
I have products for all manufacturers...

Want lots of colour!
Online ordering system with payment options online

This is a sales only website....

A site that sells similar products is:
http://e.vantelmo.cn/
I want my website to be very similar to this one.

Im basically selling these products here in australia. So I really want something "australian themed" (kangaroo or koala or australia map....)this kind of thing

Looking to attract business from car dealerships and the public.

I have attached a copy of my brochure, and some of the products I sell

```html
<!DOCTYPE html>
<html lang="en">
<head>
<meta charset="utf-8">
<title>Marbury Designs — GPS that's shaped to suit</title>
<link rel="stylesheet" href="https://fonts.googleapis.com/css2?family=Open+Sans:ital,wght@0,300;0,400;0,600;0,700;0,800;1,400&display=swap">
<style>
:root{
  --blue:#0a86c9;
  --blue-dark:#0569a6;
  --orange:#f26a21;
  --orange-soft:#f7931e;
  --ink:#333a3f;
  --grey:#777;
  --footer:#1f1f1f;
  --white:#fff;
}
*{margin:0;padding:0;box-sizing:border-box}
html,body{width:855px;height:1200px;overflow:hidden}
body{font-family:"Open Sans",Arial,sans-serif;background:#f4f4f4;position:relative;color:var(--ink)}
.abs{position:absolute}

/* top bar */
.topbar{left:0;top:0;width:855px;height:26px;background:var(--blue)}
.social{display:flex;gap:3px}
.social span{width:14px;height:14px;border-radius:50%;background:var(--white);display:block}
.topbar .social{position:absolute;left:70px;top:6px}
.contact-line{position:absolute;right:70px;top:4px;color:var(--white);font-size:13px;display:flex;gap:10px;align-items:center}
.contact-line svg{vertical-align:-2px;margin-right:4px}

/* header */
.header{left:0;top:26px;width:855px;height:60px;background:linear-gradient(#fff,#ececec);border-bottom:1px solid #ddd}
.brand{position:absolute;left:70px;top:14px;display:flex;align-items:center;gap:7px}
.brand-mark{width:30px;height:30px;background:var(--blue);border-radius:4px}
.brand-name{font-size:19px;font-weight:700;color:var(--blue);line-height:1}
.nav{position:absolute;right:70px;top:0;height:60px;display:flex;font-size:9.5px;font-weight:600;color:var(--blue-dark)}
.nav a{display:flex;align-items:center;padding:0 12px;text-decoration:none;color:inherit}
.nav a.active{background:var(--orange);color:var(--white)}

/* hero */
.hero{left:0;top:86px;width:855px;height:390px;overflow:hidden;
  background:linear-gradient(100deg,#f59a25 0%,#ef8a1c 28%,#c86a18 42%,#5e3616 58%,#24160e 76%,#3a2414 100%)}
.hero-visual{position:absolute;inset:0;
  background:
    radial-gradient(ellipse 170px 95px at 440px 85px,rgba(60,62,64,.95),rgba(60,62,64,.85) 70%,transparent 72%),
    radial-gradient(ellipse 120px 70px at 450px 80px,rgba(210,200,170,.55),transparent 75%),
    radial-gradient(ellipse 90px 70px at 720px 230px,rgba(255,235,200,.55),transparent 70%),
    radial-gradient(ellipse 260px 200px at 700px 260px,rgba(120,70,30,.55),transparent 70%),
    radial-gradient(ellipse 160px 120px at 120px 60px,rgba(255,200,90,.45),transparent 70%),
    radial-gradient(ellipse 200px 90px at 760px 40px,rgba(20,14,10,.8),transparent 70%)}
.hero-tri{position:absolute;left:0;top:0}
.hero h1{position:absolute;left:73px;top:72px;color:var(--white);font-size:56px;line-height:46px;font-weight:800;letter-spacing:-.5px}
.hero h1 .light{font-weight:300}
.hero p.lead{position:absolute;left:75px;top:170px;width:240px;color:var(--white);font-size:11.5px;font-weight:600;line-height:13.5px}
.features{position:absolute;left:75px;top:218px;color:var(--white);font-size:11.5px;line-height:20px;word-spacing:1px}
.features span{margin-right:14px}
.btn-start{position:absolute;left:75px;top:279px;width:134px;height:36px;background:var(--blue);border-bottom:3px solid var(--blue-dark);color:var(--white);font-size:14px;font-weight:600;display:flex;align-items:center;justify-content:center;gap:6px}
.dots{position:absolute;left:388px;top:346px;display:flex;gap:8px;align-items:center}
.dots span{width:20px;height:20px;border-radius:50%;background:var(--blue)}
.dots span.on{background:var(--white);box-shadow:0 0 0 2px rgba(255,255,255,.5)}

/* welcome */
.section-title{font-size:34px;font-weight:700;color:var(--ink);letter-spacing:-.5px;line-height:1}
.section-title em{font-style:normal;font-weight:400;color:var(--blue)}
.welcome{left:70px;top:508px;width:421px}
.welcome-photo{margin-top:15px;width:421px;height:128px;
  background:
    radial-gradient(ellipse 70px 60px at 150px 40px,rgba(215,190,170,.85),transparent 75%),
    radial-gradient(ellipse 40px 25px at 350px 75px,rgba(110,150,190,.8),transparent 75%),
    linear-gradient(180deg,transparent 50%,rgba(20,20,22,.85) 70%,#141416 100%),
    linear-gradient(90deg,#2a2b2d 0%,#6c6e70 25%,#d8d9da 45%,#e8e8e8 70%,#bfc1c3 100%)}
.welcome p{font-size:9px;line-height:15.5px;color:var(--grey);margin-top:9px}
.welcome p + p{margin-top:15px}

.news{left:539px;top:508px;width:250px}
.news-item{display:flex;gap:20px}
.news-thumb{width:60px;height:56px;flex:none;
  background:radial-gradient(ellipse 22px 18px at 32px 24px,rgba(120,170,210,.9),transparent 80%),linear-gradient(135deg,#6a7480,#262a2e 70%,#101214)}
.news-thumb.t2{background:radial-gradient(ellipse 18px 22px at 36px 28px,rgba(220,200,120,.85),transparent 80%),linear-gradient(135deg,#8a9098,#2a2c30 60%,#1a1012)}
.news-thumb.t3{background:radial-gradient(ellipse 16px 20px at 40px 18px,rgba(200,210,220,.85),transparent 80%),linear-gradient(135deg,#9aa0a6,#3a3c40 55%,#141416)}
.news-thumb.active{outline:4px solid var(--orange-soft)}
.news-copy{width:140px}
.news-item h3{font-size:8.5px;font-style:italic;font-weight:400;color:var(--blue);line-height:14.5px}
.news-item p{font-size:8.5px;color:var(--grey);line-height:16px;margin-top:3px}

/* clients */
.clients{left:0;top:810px;width:855px;height:274px;overflow:hidden;
  background:
    radial-gradient(ellipse 200px 160px at 80px 200px,rgba(90,92,95,.6),transparent 70%),
    radial-gradient(ellipse 220px 110px at 560px 210px,rgba(60,70,90,.7),transparent 70%),
    linear-gradient(100deg,#3a3c3e,#161819 40%,#1e2328 70%,#2a3440)}
.clients-tri{position:absolute;right:0;top:0}
.clients-inner{position:absolute;left:0;top:0;width:855px;text-align:center;color:var(--white)}
.clients h2{margin-top:23px;font-size:27px;font-weight:600;line-height:1}
.clients h2 em{font-style:normal;color:var(--orange-soft)}
.clients .sub{font-size:14px;margin-top:5px}
.clients .quote{font-size:9.6px;line-height:15px;width:575px;margin:27px auto 0}
.avatar{width:58px;height:58px;border-radius:50%;border:3px solid var(--white);background:linear-gradient(#d6d8da,#3e4a58);margin:21px auto 0}
.clients .name{font-size:11px;margin-top:8px;line-height:14px}
.arrow{position:absolute;top:114px}

/* newsletter */
.newsletter{left:0;top:1084px;width:855px;height:55px;background:var(--blue)}
.touch{position:absolute;left:88px;top:8px;color:var(--orange-soft);font-size:18px;font-weight:600;line-height:1}
.touch .phone{color:var(--white);font-size:12px;font-weight:600;margin-top:5px;display:flex;align-items:center;gap:4px}
.signup{position:absolute;left:278px;top:8px;color:var(--white)}
.signup h4{font-size:18px;font-weight:600;line-height:1}
.signup p{font-size:11px;margin-top:5px}
.subscribe-box{position:absolute;left:498px;top:8px;width:287px;height:39px;background:var(--white);border-radius:2px}
.subscribe-box .placeholder{position:absolute;left:11px;top:14px;font-size:8px;font-style:italic;color:#aaa}
.subscribe-box .btn{position:absolute;right:7px;top:5px;width:90px;height:28px;background:var(--orange);color:var(--white);font-size:11px;font-weight:700;display:flex;align-items:center;justify-content:center}

/* footer */
.footer{left:0;top:1139px;width:855px;height:61px;background:var(--footer);color:var(--white);font-size:8px}
.footer .copy{position:absolute;left:89px;top:24px}
.footer .links{position:absolute;left:328px;top:25px;display:flex;gap:7px}
.footer .social{position:absolute;left:717px;top:22px}
.footer .social span{background:#777}
</style>
</head>
<body>

<div class="abs topbar">
  <div class="social"><span></span><span></span><span></span><span></span></div>
  <div class="contact-line">
    <span><svg width="14" height="10" viewBox="0 0 14 10"><rect width="14" height="10" fill="#f7931e"/><path d="M0 0l7 6 7-6" stroke="#fff" stroke-width="1.2" fill="none"/></svg>info@marburydesigns.com</span>
    <span><svg width="13" height="13" viewBox="0 0 13 13"><circle cx="6.5" cy="6.5" r="5.8" fill="none" stroke="#f7931e" stroke-width="1.2"/><path d="M4.3 3.5l1.3 1.3-.8.9a5 5 0 0 0 2.4 2.4l.9-.8 1.3 1.3-.9.9C6.5 9.4 3.6 6.5 3.5 4.4z" fill="#f7931e"/></svg>02 5550 1938</span>
  </div>
</div>

<header class="abs header">
  <div class="brand"><span class="brand-mark"></span><span class="brand-name">Marbury Designs</span></div>
  <nav class="nav">
    <a class="active">HOME</a><a>PRODUCTS</a><a>SERVICES</a><a>ABOUT US</a><a>NEWS</a><a>CONTACT</a>
  </nav>
</header>

<section class="abs hero">
  <div class="hero-visual" role="img" aria-label="GPS that's shaped to suit: in-dash navigation unit in front of a sports car at sunset on an Australian road"></div>
  <svg class="hero-tri" width="855" height="390" viewBox="0 0 855 390"><polygon points="165,0 350,390 60,390" fill="#ffb040" opacity=".18"/><polygon points="290,0 520,0 350,390" fill="#fff" opacity=".05"/></svg>
  <h1>Better<br>Than <span class="light">Better</span></h1>
  <p class="lead">Lorem ipsum dolor sit amet, consectetuer adipiscing elit, sed diam nonummy nibh euismod tincidunt ut laoreet.</p>
  <div class="features">
    <div><span>1s Accele-Boot</span><span>Free Voice Control</span></div>
    <div><span>Connect wonderful life</span><span>Customize your UI style</span></div>
  </div>
  <div class="btn-start">
    <svg width="16" height="16" viewBox="0 0 16 16"><path d="M9 2h5v12H9" stroke="#fff" stroke-width="2" fill="none"/><path d="M1 8h8M6 4.5L9.5 8 6 11.5" stroke="#fff" stroke-width="2.4" fill="none"/></svg>
    Get Started
  </div>
  <div class="dots"><span class="on"></span><span></span><span></span></div>
</section>

<section class="abs welcome">
  <h2 class="section-title">Welcome <em>To Marbury</em></h2>
  <div class="welcome-photo" role="img" aria-label="Driver at the wheel beside a built-in dashboard navigation screen"></div>
  <p>Duis autem vel eum iriure dolor in hendrerit in vulputate velit esse molestie consequat, illum dolore eu feugiat nulla facilisis at vero eros et accumsan et iusto odio Claritas est etiam processus dynamicus, qui sequitur mutationem</p>
  <p>consuetudium lectorum. Mirum est notare quam littera gothica, quam nunc putamus parum claram, anteposuerit litterarum lorem ipsum dolo</p>
</section>

<section class="abs news">
  <h2 class="section-title">Latest <em>News</em></h2>
  <div class="news-item" style="margin-top:16px">
    <div class="news-thumb active" role="img" aria-label="Hand touching a car navigation screen"></div>
    <div class="news-copy"><h3>Duis autem vel eum iriure dolor in hendrerit in vulputate ve...</h3><p>Lorem ipsum dolor sit amet, con-stuer adipiscing</p></div>
  </div>
  <div class="news-item" style="margin-top:24px">
    <div class="news-thumb t2" role="img" aria-label="GPS unit mounted on a car dashboard"></div>
    <div class="news-copy"><h3>Duis autem vel eum iriure dolor in hendrerit in vulputate ve...</h3><p>Lorem ipsum dolor sit amet, con-stuer adipiscing</p></div>
  </div>
  <div class="news-item" style="margin-top:24px">
    <div class="news-thumb t3" role="img" aria-label="Driver holding a GPS device"></div>
    <div class="news-copy"><h3>Duis autem vel eum iriure dolor in hendrerit in vulputate ve...</h3><p>Lorem ipsum dolor sit amet, con-stuer adipiscing</p></div>
  </div>
</section>

<section class="abs clients" role="img" aria-label="Car dashboard interior with navigation display">
  <svg class="clients-tri" width="200" height="274" viewBox="0 0 200 274"><polygon points="0,0 200,0 200,274 60,274 120,180" fill="#0a86c9" opacity=".7"/></svg>
  <div class="clients-inner">
    <h2>Our <em>Clients</em></h2>
    <div class="sub">We Value The Quality First</div>
    <p class="quote">Lorem Ipsum is simply dummy text of the printing and typesetting the readable content of a page when looking at its layout. The point of using Lorem Ipsum is it has a more-or-less normal distribution of letters, as opposed readable English.</p>
    <div class="avatar" role="img" aria-label="Client portrait"></div>
    <div class="name">Sam Porter<br>General Manager Novatrek</div>
  </div>
  <svg class="arrow" style="left:70px" width="22" height="42" viewBox="0 0 22 42"><path d="M20 1L2 21l18 20" stroke="#fff" stroke-width="2" fill="none"/></svg>
  <svg class="arrow" style="left:770px" width="22" height="42" viewBox="0 0 22 42"><path d="M2 1l18 20L2 41" stroke="#fff" stroke-width="2" fill="none"/></svg>
</section>

<section class="abs newsletter">
  <div class="touch">Get in Touch
    <div class="phone"><svg width="14" height="14" viewBox="0 0 13 13"><circle cx="6.5" cy="6.5" r="5.8" fill="none" stroke="#f7931e" stroke-width="1.2"/><path d="M4.3 3.5l1.3 1.3-.8.9a5 5 0 0 0 2.4 2.4l.9-.8 1.3 1.3-.9.9C6.5 9.4 3.6 6.5 3.5 4.4z" fill="#f7931e"/></svg>(0800) 555-0142</div>
  </div>
  <div class="signup"><h4>Sign up for Newsletter</h4><p>Marbury eu feugiat nulla facilisis at</p></div>
  <div class="subscribe-box"><span class="placeholder">Your Email Address</span><span class="btn">SUBSCRIBE</span></div>
</section>

<footer class="abs footer">
  <div class="copy">© 2014 Marbury Designs All rights reserved.</div>
  <div class="links"><span>About us</span><span>|</span><span>Terms of use</span><span>|</span><span>Privacy policy</span><span>|</span><span>Contact</span></div>
  <div class="social"><span></span><span></span><span></span><span></span></div>
</footer>

</body>
</html>
```